Poster Design Project

Simple, very easy design project.

Design for a 20" x 30" poster (I will print the poster, you do the high-res design), of the attached.

(Pls note, this JPG is sideways and is an error). You are designing PORTRAIT

```html
<!DOCTYPE html>
<html lang="en">
<head>
<meta charset="utf-8">
<title>Great Ecommerce Poster</title>
<link href="https://fonts.googleapis.com/css2?family=Orbitron:wght@500&family=Encode+Sans+Condensed:wght@400&display=swap" rel="stylesheet">
<style>
  :root {
    --page: #ffffff;
    --poster: #000000;
    --title-blue: #1869b3;
    --glow-cyan: #3fd6f0;
    --glow-deep: #0a5f78;
    --panel-top: #6fd3ea;
    --panel-mid: #1a7f9e;
    --panel-bottom: #06222c;
    --value-text: #ffffff;
    --value-shadow: #1a1a1a;
  }
  * { margin: 0; padding: 0; box-sizing: border-box; }
  html, body { width: 825px; height: 1200px; overflow: hidden; background: var(--page); }
  .poster {
    position: absolute;
    left: 37px; top: 31px;
    width: 750px; height: 1127px;
    background: var(--poster);
    overflow: hidden;
  }
  .title {
    position: absolute;
    left: 0; right: 0; top: 118px;
    text-align: center;
    font-family: "Orbitron", sans-serif;
    font-weight: 500;
    color: var(--title-blue);
    line-height: 90px;
    letter-spacing: 1px;
  }
  .title-line { display: block; font-size: 88px; }
  .title-line.wide { font-size: 89px; letter-spacing: -2px; }
  .sparkle-field {
    position: absolute;
    left: 0; top: 385px;
    width: 750px; height: 650px;
    background:
      radial-gradient(ellipse 46% 10% at 50% 11%, rgba(63,214,240,0.55), transparent 70%),
      radial-gradient(ellipse 48% 9% at 45% 86%, rgba(63,214,240,0.6), transparent 70%),
      radial-gradient(ellipse 14% 30% at 13% 45%, rgba(63,214,240,0.4), transparent 70%),
      radial-gradient(ellipse 14% 25% at 88% 62%, rgba(63,214,240,0.35), transparent 70%),
      radial-gradient(ellipse 60% 45% at 50% 55%, rgba(10,95,120,0.45), transparent 75%);
  }
  .panel {
    position: absolute;
    left: 143px; top: 478px;
    width: 458px; height: 459px;
    background: linear-gradient(170deg, var(--panel-top) 0%, var(--panel-mid) 35%, #0d4a5e 65%, var(--panel-bottom) 100%);
    opacity: 0.85;
  }
  .values {
    position: absolute;
    left: 0; right: 0; top: 548px;
    list-style: none;
    text-align: center;
    font-family: "Encode Sans Condensed", sans-serif;
    font-size: 43px;
    line-height: 49.5px;
    letter-spacing: -1px;
    color: var(--value-text);
    text-shadow: 0 0 2px var(--value-shadow), 1px 1px 3px var(--value-shadow), 0 0 6px rgba(0,0,0,0.7);
  }
</style>
</head>
<body>
  <main class="poster">
    <h1 class="title">
      <span class="title-line">GREAT</span>
      <span class="title-line wide">ECOMMERCE</span>
    </h1>
    <div class="sparkle-field" role="img" aria-label="Swirling ribbon of glowing cyan light particles around a square"></div>
    <div class="panel" aria-hidden="true"></div>
    <ul class="values">
      <li>Diversity Of Thought</li>
      <li>Desire To Learn</li>
      <li>Never Settle</li>
      <li>Be A Problem Solver</li>
      <li>Work Fast (Web Speed)</li>
      <li>Execution - A Way Of Life</li>
    </ul>
  </main>
</body>
</html>
```